Pamphlet that will be placed inside hotel rooms for laundry service

We are offering all guests of a Hotel property in NYC next day laundry services.

Things to include on the flyer-
COMPLEMENTARY pick up and delivery
COMPLEMENTARY Brisko and Fluffel!
NEXT DAY SERVICE
Smells great
We keep Colors Brighter!
Next day delivery
1.10/Lb.
Email notifications
Please use our logo and the logo of hotel (attached)

All they have to do is place an order at www.quikwashora.com and leave it by the front desk at the hotel,

All laundry will be delivered next day professionally folded

Target Market(s)

this will be going inside very fancy hotels
we are looking for a clean look nothing to busy

Industry/Entity Type

Hotel

Font styles to use
Other font styles liked:
• Harababa

Requirements
Must have
• The font and color codes for the logo are as follows:
• Logo font: Harabara
• Slogan font: Swiss 721 Light Extended BT
• Dark blue: C 100 M 88 Y 0 K 0
• Light blue: C 85 M 50 Y 0 K 0
• Orange: C 0 M 80 Y 95 K 0
• Violet: C 85 M 100 Y 0 K 0

```html
<!DOCTYPE html>
<html lang="en">
<head>
<meta charset="utf-8">
<title>Quikwashora Laundry Service – Hotel Quenvarre</title>
<link rel="stylesheet" href="https://fonts.googleapis.com/css2?family=Inter:wght@300;400;800;900&display=swap">
<style>
  :root {
    --blue-deep: #0b5ba8;
    --blue-brand: #1f64b8;
    --violet-grey: #6c6a86;
    --ink: #1d2f45;
    --ink-dark: #1a1a1a;
    --white: #ffffff;
  }
  * { margin: 0; padding: 0; box-sizing: border-box; }
  html, body { width: 1200px; height: 919px; overflow: hidden; background: var(--white); }
  .flyer {
    position: relative;
    width: 1200px;
    height: 919px;
    overflow: hidden;
    font-family: "Inter", Helvetica, Arial, sans-serif;
    background: var(--white);
  }
  .backdrop { position: absolute; inset: 0; }

  .features {
    position: absolute;
    left: 162px;
    top: 84px;
    list-style: none;
  }
  .features li {
    display: flex;
    align-items: center;
    height: 59px;
    font-size: 45px;
    font-weight: 300;
    letter-spacing: -0.8px;
    color: var(--ink);
    text-shadow: 0 0 6px var(--white), 0 0 12px rgba(255,255,255,0.9), 0 0 20px rgba(255,255,255,0.6);
  }
  .features li::before {
    content: "";
    flex: none;
    width: 18px;
    height: 18px;
    margin-right: 12px;
    border: 1.5px solid var(--ink);
    background: rgba(255,255,255,0.85);
    box-shadow: 0 0 6px var(--white);
  }

  .instructions {
    position: absolute;
    left: 166px;
    top: 592px;
    width: 625px;
    font-size: 17px;
    font-weight: 900;
    line-height: 1.25;
    color: var(--ink-dark);
  }
  .instructions p + p { margin-top: 22px; }

  .laundry-basket {
    position: absolute;
    left: 717px;
    top: 738px;
    width: 144px;
    height: 106px;
    border-radius: 40% 40% 30% 30%;
    background: radial-gradient(ellipse at 50% 40%, #e8533a 0%, #c8362a 55%, #1f5fb0 100%);
  }

  .laundry-brand {
    position: absolute;
    left: 660px;
    top: 852px;
    width: 260px;
    text-align: center;
  }
  .laundry-brand .name {
    font-size: 29px;
    font-weight: 800;
    letter-spacing: -0.3px;
    color: var(--blue-brand);
    line-height: 1;
  }
  .laundry-brand .slogan {
    margin-top: 6px;
    font-size: 12px;
    font-weight: 400;
    letter-spacing: 1px;
    color: var(--ink);
  }

  .hotel-brand {
    position: absolute;
    left: 946px;
    top: 838px;
    width: 240px;
    font-size: 30px;
    font-weight: 800;
    letter-spacing: 2px;
    color: var(--violet-grey);
    line-height: 1.1;
  }
</style>
</head>
<body>
<div class="flyer">
  <svg class="backdrop" width="1200" height="919" viewBox="0 0 1200 919" aria-hidden="true">
    <defs>
      <linearGradient id="sky" x1="0" y1="0" x2="0" y2="1">
        <stop offset="0" stop-color="#0a58a6"/>
        <stop offset="0.4" stop-color="#1c6db7"/>
        <stop offset="0.68" stop-color="#6e9ed2"/>
        <stop offset="0.82" stop-color="#b4cce7"/>
        <stop offset="1" stop-color="#d9e5f3"/>
      </linearGradient>
      <linearGradient id="band" x1="0" y1="0" x2="1" y2="0">
        <stop offset="0" stop-color="#0b5ba8"/>
        <stop offset="0.55" stop-color="#3a7fc3"/>
        <stop offset="1" stop-color="#b9d0ea"/>
      </linearGradient>
    </defs>
    <path d="M0 0 H1200 V180 C1150 470 930 700 600 780 C400 825 180 835 0 830 Z" fill="url(#sky)"/>
    <path d="M0 770 C260 800 520 790 760 730 C620 790 420 830 0 830 Z" fill="url(#band)"/>
    <path d="M1200 210 C1160 470 980 660 720 748" fill="none" stroke="#ffffff" stroke-width="6" stroke-opacity="0.9"/>
    <path d="M1180 0 C1200 60 1200 120 1200 180 V0 Z" fill="#ffffff"/>
  </svg>

  <ul class="features">
    <li>COMPLEMENTARY pick up and delivery</li>
    <li>COMPLEMENTARY Brisko and Fluffel!</li>
    <li>NEXT DAY SERVICE</li>
    <li>Smells great</li>
    <li>We keep Colors Brighter!</li>
    <li>Next day delivery</li>
    <li>1.10/Lb.</li>
    <li>Email notifications</li>
  </ul>

  <div class="instructions">
    <p>place an order at www.quikwashora.com and leave it by the front desk at the hotel,</p>
    <p>All laundry will be delivered next day professionally folded</p>
  </div>

  <div class="laundry-basket" role="img" aria-label="Illustration of a laundry basket filled with colourful clothes"></div>

  <div class="laundry-brand">
    <div class="name">quikwashora.com</div>
    <div class="slogan">Fresh. Folded. Delivered.</div>
  </div>

  <div class="hotel-brand">
    <div>HOTEL</div>
    <div>QUENVARRE</div>
  </div>
</div>
</body>
</html>
```